Prepared Meal Company Needs Menu Design

We are a pre-prepared meal delivery company called Greel Brantwick.

We have a menu in excel but needs to be designed to look good and appealing to customers. The menu should be clean, easy to ready, and show:Title (Pupusa)Tags (V, V+, GF - Use a cool vegan logo for the V+ and logo for vegetarian V symbol)Price (12.99)DescriptionBrand colors are orange white and green. Design is clean, crisp and can incorporate natural elements like leaf shaped symbols, etc. Screenshots from our website attached for inspiration.

Target Market(s)

Broad demographics

Industry/Entity Type

Restaurant

Font styles to use
Sans Serif

Requirements
Must have
• The menu design should be commensurate with the website under development
• https://greelbrantwick.tavlorix.com
Nice to have
• Should have appropriate graphics
Should not have
• Modifiers do not need to be shown (these are shown in the excel only).

```html
<!DOCTYPE html>
<html lang="en">
<head>
<meta charset="utf-8">
<title>Greel Brantwick Menu</title>
<link rel="stylesheet" href="https://fonts.googleapis.com/css2?family=Arimo:wght@400;700&family=Exo+2:ital,wght@1,400&display=swap">
<style>
  :root {
    --orange: #ff6a0d;
    --green: #1f8a3c;
    --green-dark: #17702f;
    --ink: #3a3a3a;
    --paper: #ffffff;
    --backdrop: #ffffff;
  }
  * { box-sizing: border-box; margin: 0; padding: 0; }
  html, body { width: 1200px; height: 2604px; overflow: hidden; background: var(--backdrop); }
  body { position: relative; font-family: "Arimo", Arial, sans-serif; color: var(--ink); }

  .menu-page {
    position: absolute; left: 92px; width: 1012px;
    background: var(--paper);
    box-shadow: 0 3px 14px rgba(0,0,0,0.22);
    overflow: hidden;
  }
  .menu-page--one { top: 70px; height: 1228px; }
  .menu-page--two { top: 1344px; height: 1228px; }

  .brand { position: absolute; left: 40px; top: 38px; display: flex; align-items: center; gap: 12px; }
  .brand-dot { width: 52px; height: 52px; border-radius: 50%; background: var(--orange); }
  .brand-name { font-weight: 700; font-size: 24px; color: var(--orange); }

  .section-band {
    position: absolute; left: 548px; right: 0; height: 34px;
    background: var(--orange); color: #fff;
    font-weight: 700; font-size: 22px; line-height: 34px; padding-left: 20px;
  }

  .page-foot { position: absolute; left: 0; right: 0; bottom: 0; height: 24px; background: var(--orange); }

  .item { position: absolute; left: 0; right: 0; }
  .item-name {
    position: absolute; left: 98px; width: 420px;
    font-weight: 700; font-size: 20px; line-height: 24px; color: var(--green);
  }
  .item-price {
    position: absolute; left: 447px; width: 120px; text-align: right;
    font-weight: 700; font-size: 21px; line-height: 24px; color: var(--ink);
  }
  .item-desc {
    position: absolute; left: 622px; width: 362px; top: 4px;
    font-family: "Exo 2", Arial, sans-serif; font-style: italic;
    font-size: 13px; line-height: 18px; color: var(--ink);
  }
  .item-tags {
    position: absolute; left: 371px; display: flex; align-items: center; gap: 6px;
    font-weight: 700; font-size: 16px; color: var(--ink);
  }
  .item-tags--plain { left: 406px; }
  .badge { width: 40px; height: 40px; display: block; }

  .divider {
    position: absolute; left: 83px; width: 812px; height: 0;
    border-top: 2px dashed var(--orange); opacity: 0.75;
  }
</style>
</head>
<body>

<section class="menu-page menu-page--one">
  <div class="brand"><span class="brand-dot"></span><span class="brand-name">Greel Brantwick</span></div>

  <div class="section-band" style="top:122px">BREAKFAST &nbsp;- All Menu Items Soy Free</div>

  <div class="item" style="top:200px">
    <div class="item-name">Cinnamon-Apple Sunrise Oats</div>
    <div class="item-price">6.99</div>
    <p class="item-desc">Almond Milk &amp; Ceylon Cinnamon, Marinated Golden Raisins, Macca Powder, Apple-Pecan Crumble</p>
    <div class="item-tags" style="top:34px"><svg class="badge" viewBox="0 0 40 40" role="img" aria-label="Vegan badge"><circle cx="20" cy="20" r="19" fill="var(--green)"/><circle cx="20" cy="20" r="14" fill="none" stroke="#fff" stroke-width="2"/></svg>GF</div>
  </div>
  <div class="divider" style="top:281px"></div>

  <div class="item" style="top:293px">
    <div class="item-name">Acai Yogurt</div>
    <div class="item-price">7.99</div>
    <p class="item-desc">Coconut, Goji, Seasonal Fruit, Crunchy Chia Seeds, Ceylon Cinnamon</p>
    <div class="item-tags" style="top:34px"><svg class="badge" viewBox="0 0 40 40" role="img" aria-label="Vegetarian badge"><circle cx="20" cy="20" r="17" fill="#fff" stroke="var(--green)" stroke-width="4"/><circle cx="20" cy="20" r="8" fill="var(--green)"/></svg>GF</div>
  </div>
  <div class="divider" style="top:373px"></div>

  <div class="item" style="top:385px">
    <div class="item-name">Orvane 4:9 Cereal &amp; Yogurt</div>
    <div class="item-price">7.49</div>
    <p class="item-desc">Apricot-Pear Compote, Almond &amp; Seba Drizzle</p>
    <div class="item-tags" style="top:34px"><svg class="badge" viewBox="0 0 40 40" role="img" aria-label="Vegetarian badge"><circle cx="20" cy="20" r="17" fill="#fff" stroke="var(--green)" stroke-width="4"/><circle cx="20" cy="20" r="8" fill="var(--green)"/></svg></div>
  </div>
  <div class="divider" style="top:465px"></div>

  <div class="item" style="top:472px">
    <div class="item-name">St. Benedict's Eggs</div>
    <div class="item-price">9.49</div>
    <p class="item-desc">2 Soft Yolk Eggs over Rosemary Polenta, Caramelized Onion, Mushrooms &amp; Asparagus, Lemon</p>
    <div class="item-tags" style="top:34px"><svg class="badge" viewBox="0 0 40 40" role="img" aria-label="Vegetarian badge"><circle cx="20" cy="20" r="17" fill="#fff" stroke="var(--green)" stroke-width="4"/><circle cx="20" cy="20" r="8" fill="var(--green)"/></svg>Dairy Free</div>
  </div>
  <div class="divider" style="top:552px"></div>

  <div class="item" style="top:560px">
    <div class="item-name">Pomegranate &amp; Saffron Shakshuka</div>
    <div class="item-price">10.99</div>
    <p class="item-desc">2 Soft Yolk Eggs over Roasted Tomatoes, Onions &amp; Peppers, Garden Herb Oil, Rosemary, Oregano &amp; Thyme with Handmade Gluten-Free Flatbread</p>
    <div class="item-tags" style="top:34px"><svg class="badge" viewBox="0 0 40 40" role="img" aria-label="Vegetarian badge"><circle cx="20" cy="20" r="17" fill="#fff" stroke="var(--green)" stroke-width="4"/><circle cx="20" cy="20" r="8" fill="var(--green)"/></svg>GF Dairy Free</div>
  </div>
  <div class="divider" style="top:650px"></div>

  <div class="item" style="top:677px">
    <div class="item-name">Sweet Potato Hash</div>
    <div class="item-price">8.99</div>
    <p class="item-desc">Broccolini, Cherry Tomato, Asparagus, Roasted Peppers &amp; Onions, Rosemary-Nutritional Yeast</p>
    <div class="item-tags" style="top:34px"><svg class="badge" viewBox="0 0 40 40" role="img" aria-label="Vegan badge"><circle cx="20" cy="20" r="19" fill="var(--green)"/><circle cx="20" cy="20" r="14" fill="none" stroke="#fff" stroke-width="2"/></svg>GF</div>
  </div>
  <div class="divider" style="top:751px"></div>

  <div class="item" style="top:767px">
    <div class="item-name">Mom's Frittata</div>
    <div class="item-price">11.99</div>
    <p class="item-desc">Roasted Cherry Tomato, Goat Cheese &amp; Baby Spinach with Sweet Potato Homefries</p>
    <div class="item-tags" style="top:34px"><svg class="badge" viewBox="0 0 40 40" role="img" aria-label="Vegetarian badge"><circle cx="20" cy="20" r="17" fill="#fff" stroke="var(--green)" stroke-width="4"/><circle cx="20" cy="20" r="8" fill="var(--green)"/></svg>GF</div>
  </div>
  <div class="divider" style="top:847px"></div>

  <div class="item" style="top:865px">
    <div class="item-name">Country Style Breakfast Sandwich</div>
    <div class="item-price">13.99</div>
    <p class="item-desc">Arugula, Goat Cheese, Cherry Tomatoes &amp; Lemon with Mom's Frittata on Orvane 4:9 Bread</p>
    <div class="item-tags" style="top:34px"><svg class="badge" viewBox="0 0 40 40" role="img" aria-label="Vegetarian badge"><circle cx="20" cy="20" r="17" fill="#fff" stroke="var(--green)" stroke-width="4"/><circle cx="20" cy="20" r="8" fill="var(--green)"/></svg></div>
  </div>

  <div class="section-band" style="top:945px">APPETIZERS</div>

  <div class="item" style="top:1003px">
    <div class="item-name">Avocado Super-Toast</div>
    <div class="item-price">9.49</div>
    <p class="item-desc">Shaved Fennel &amp; Golden Beets, Avocado, Garden Herb Oil, Lemon Juice, Ground Flax, Hemp Seed, Golden Raisin &amp; Moringa on Orvane 4:9 Sprouted Whole</p>
    <div class="item-tags" style="top:34px"><svg class="badge" viewBox="0 0 40 40" role="img" aria-label="Vegan badge"><circle cx="20" cy="20" r="19" fill="var(--green)"/><circle cx="20" cy="20" r="14" fill="none" stroke="#fff" stroke-width="2"/></svg>GF with Flatbread</div>
  </div>
  <div class="divider" style="top:1085px"></div>

  <div class="item" style="top:1107px">
    <div class="item-name">Pupusa</div>
    <div class="item-price">9.49</div>
    <p class="item-desc" style="top:16px">Coconut, Goji, Seasonal Fruit, Crunchy Chia Seeds, Ceylon Cinnamon</p>
    <div class="item-tags" style="top:30px"><svg class="badge" viewBox="0 0 40 40" role="img" aria-label="Vegetarian badge"><circle cx="20" cy="20" r="17" fill="#fff" stroke="var(--green)" stroke-width="4"/><circle cx="20" cy="20" r="8" fill="var(--green)"/></svg>GF</div>
  </div>

  <div class="page-foot"></div>
</section>

<section class="menu-page menu-page--two">
  <div class="brand"><span class="brand-dot"></span><span class="brand-name">Greel Brantwick</span></div>

  <div class="item" style="top:147px">
    <div class="item-name">Pupusa Deluxe</div>
    <div class="item-price">13.99</div>
    <p class="item-desc">Sous Vide Bison Shortrib, Goat Cheese, Ayocote &amp; Avocado Puree, Nopales, Cilantro-Lime Yogurt, Inca Corn Crumble, Tropical Acai Hot Sauce</p>
    <div class="item-tags item-tags--plain" style="top:30px">GF</div>
  </div>
  <div class="divider" style="top:210px"></div>

  <div class="item" style="top:224px">
    <div class="item-name">Egyptian Flatbread</div>
    <div class="item-price">11.99</div>
    <p class="item-desc">Honey-Chamomile Yogurt, Braised Cherry Tomatoes, Sumac &amp; Pistachio Dukkha, Garlic &amp; Micro Radish on Handmade Gluten-Free Flatbread</p>
    <div class="item-tags" style="top:34px"><svg class="badge" viewBox="0 0 40 40" role="img" aria-label="Vegetarian badge"><circle cx="20" cy="20" r="17" fill="#fff" stroke="var(--green)" stroke-width="4"/><circle cx="20" cy="20" r="8" fill="var(--green)"/></svg>GF</div>
  </div>
  <div class="divider" style="top:305px"></div>

  <div class="item" style="top:328px">
    <div class="item-name">Green Street Tacos</div>
    <div class="item-price">9.99</div>
    <p class="item-desc">Sugar Snap Peas, Guacamole, Radish &amp; Inca Corn Crumble on 2 Handmade Corn Tortillas.</p>
    <div class="item-tags" style="top:34px"><svg class="badge" viewBox="0 0 40 40" role="img" aria-label="Vegan badge"><circle cx="20" cy="20" r="19" fill="var(--green)"/><circle cx="20" cy="20" r="14" fill="none" stroke="#fff" stroke-width="2"/></svg>GF</div>
  </div>
  <div class="divider" style="top:406px"></div>

  <div class="item" style="top:427px">
    <div class="item-name">Marinated Squash Tacos</div>
    <div class="item-price">9.99</div>
    <p class="item-desc">Chayote Escebeche, Jalapeno, Guacamole, Carrots, Radish, Pepitas &amp; Cilantro, on 2 Handmade Corn Tortillas.</p>
    <div class="item-tags" style="top:34px"><svg class="badge" viewBox="0 0 40 40" role="img" aria-label="Vegetarian badge"><circle cx="20" cy="20" r="17" fill="#fff" stroke="var(--green)" stroke-width="4"/><circle cx="20" cy="20" r="8" fill="var(--green)"/></svg>GF</div>
  </div>
  <div class="divider" style="top:506px"></div>

  <div class="item" style="top:520px">
    <div class="item-name">Soft Yolk Egg &amp;<br>Avocado "Toast" Flatbread</div>
    <div class="item-price">10.99</div>
    <p class="item-desc">Ayocote &amp; Avocado Puree, Guacamole, Sunflower Seeds, Inca Corn, Arugula, Lime &amp; Soft Yolk Egg on Handmade Gluten-Free Flatbread</p>
    <div class="item-tags" style="top:52px"><svg class="badge" viewBox="0 0 40 40" role="img" aria-label="Vegetarian badge"><circle cx="20" cy="20" r="17" fill="#fff" stroke="var(--green)" stroke-width="4"/><circle cx="20" cy="20" r="8" fill="var(--green)"/></svg>GF</div>
  </div>

  <div class="section-band" style="top:620px">SOUPS</div>

  <div class="item" style="top:682px">
    <div class="item-name">Seasonal Vegetable Minestrone<br>with Free Range Turkey Meatballs</div>
    <div class="item-price">9.49</div>
    <p class="item-desc">Ayocote Beans, Roasted Tomatoes, Carrots, Onions &amp; Bell Pepper, Snap Peas, Garnett Yam, Rosemary &amp; Oregano</p>
    <div class="item-tags item-tags--plain" style="top:52px">GF</div>
  </div>
  <div class="divider" style="top:766px"></div>

  <div class="item" style="top:774px">
    <div class="item-name">Sweet Carrot &amp; Coriander Soup</div>
    <div class="item-price">5.99</div>
    <p class="item-desc">Garden Herb Oil, Cilantro, Toasted Pepita</p>
    <div class="item-tags" style="top:34px"><svg class="badge" viewBox="0 0 40 40" role="img" aria-label="Vegan badge"><circle cx="20" cy="20" r="19" fill="var(--green)"/><circle cx="20" cy="20" r="14" fill="none" stroke="#fff" stroke-width="2"/></svg>GF</div>
  </div>
  <div class="divider" style="top:851px"></div>

  <div class="item" style="top:880px">
    <div class="item-name">Butternut Squash &amp; Nopale Chili</div>
    <div class="item-price">13.99</div>
    <p class="item-desc">Arugula, Goat Cheese, Cherry Tomatoes &amp; Lemon with Mom's Frittata on Orvane 4:9 Bread</p>
    <div class="item-tags" style="top:34px"><svg class="badge" viewBox="0 0 40 40" role="img" aria-label="Vegetarian badge"><circle cx="20" cy="20" r="17" fill="#fff" stroke="var(--green)" stroke-width="4"/><circle cx="20" cy="20" r="8" fill="var(--green)"/></svg>GF Dairy Free</div>
    <div class="item-tags" style="top:86px"><svg class="badge" viewBox="0 0 40 40" role="img" aria-label="Vegan badge"><circle cx="20" cy="20" r="19" fill="var(--green)"/><circle cx="20" cy="20" r="14" fill="none" stroke="#fff" stroke-width="2"/></svg>if No Goat Cheese</div>
  </div>
  <div class="divider" style="top:1032px"></div>

  <div class="item" style="top:1037px">
    <div class="item-name">Tolver's Chicken Soup</div>
    <p class="item-desc">Gluten-Free Sorghum Penne, Root Vegetables, Oregano &amp; Peppercorns on the Vine</p>
    <div class="item-tags item-tags--plain" style="top:30px">GF with Flatbread</div>
  </div>

  <div class="page-foot"></div>
</section>

</body>
</html>
```